Business Card Design

I give lessons and clinics for dressage riders
I would like the design to be an outline (with broad lines) of a dressage horse and rider with in background of whole card with print over top tan or parchment card with burgundy print

Industry/Entity Type

Business

Contact Information for Business Card

Tod Harlick
555-317-0492
Classical dressage training for the modern American
Clinics, lessons, training level -Prix St. George

Requirements
Must have
• broad lined outline of dressage horse and rider

```html
<!DOCTYPE html>
<html lang="en">
<head>
<meta charset="utf-8">
<title>Tod Harlick – Business Card</title>
<link rel="stylesheet" href="https://fonts.googleapis.com/css2?family=Belleza&family=Alegreya+Sans:wght@800&display=swap">
<style>
  :root {
    --backdrop: #e7e2dd;
    --parchment: #f2dfd2;
    --burgundy: #8c2048;
    --tan: #e6b68e;
    --horse-tint: #ecd2bd;
  }
  html, body {
    margin: 0;
    padding: 0;
    width: 1200px;
    height: 986px;
    overflow: hidden;
    background: var(--backdrop);
  }
  .card {
    position: absolute;
    left: 58px;
    top: 176px;
    width: 1084px;
    height: 634px;
    background: var(--parchment);
    overflow: hidden;
    box-shadow: 0 2px 8px rgba(0,0,0,0.12);
  }
  .horse-rider-art {
    position: absolute;
    left: 210px;
    top: 190px;
    width: 600px;
    height: 410px;
    border-radius: 45% 40% 30% 30%;
    background: radial-gradient(ellipse at center, var(--horse-tint) 0%, rgba(236,210,189,0.5) 55%, rgba(242,223,210,0) 80%);
  }
  .swoosh {
    position: absolute;
    left: 0;
    top: 0;
    width: 1084px;
    height: 634px;
  }
  .tagline {
    position: absolute;
    left: 0;
    top: 48px;
    width: 100%;
    margin: 0;
    text-align: center;
    font-family: "Belleza", sans-serif;
    font-size: 34px;
    line-height: 48px;
    color: var(--burgundy);
  }
  .name {
    position: absolute;
    left: 0;
    top: 320px;
    width: 100%;
    margin: 0;
    text-align: center;
    font-family: "Alegreya Sans", sans-serif;
    font-weight: 800;
    font-size: 76px;
    line-height: 90px;
    color: var(--burgundy);
  }
  .phone {
    position: absolute;
    left: 0;
    top: 432px;
    width: 100%;
    text-align: center;
    font-family: "Belleza", sans-serif;
    font-size: 44px;
    line-height: 60px;
    color: var(--burgundy);
  }
  .phone-icon {
    width: 44px;
    height: 44px;
    vertical-align: -6px;
    margin-right: 10px;
  }
</style>
</head>
<body>
  <div class="card">
    <div class="horse-rider-art" role="img" aria-label="Faint broad-lined outline of a dressage horse and rider filling the card background"></div>

    <svg class="swoosh" viewBox="0 0 1084 634" aria-hidden="true">
      <path fill="var(--tan)" d="M0,392 C230,250 560,215 1000,256 C580,232 250,280 0,424 Z"/>
      <path fill="var(--burgundy)" d="M0,356 C240,212 600,180 1070,258 C600,206 250,240 0,400 Z"/>
    </svg>

    <p class="tagline">Classical Dressage Training for the Modern<br>American Clinics, Lessons,<br>Training Level -Prix St. George</p>

    <h1 class="name">Tod Harlick</h1>

    <div class="phone">
      <svg class="phone-icon" viewBox="0 0 44 44" aria-hidden="true">
        <circle cx="22" cy="22" r="17" fill="none" stroke="var(--burgundy)" stroke-width="4"/>
        <path d="M10,36 L34,8" stroke="var(--burgundy)" stroke-width="4" stroke-linecap="round"/>
        <path d="M13,27 C12,20 18,14 25,14 L27,18 L23,20 C20,21 18,24 18,27 Z" fill="var(--burgundy)"/>
      </svg>555-317-0492
    </div>
  </div>
</body>
</html>
```